CHRISTMAS CARD

We want a Christmas card for wealth managers to issue to high net worth clients. Very classy. Very corporate. The finished printed card will be a5 to fit existing envelopes. the design will also be used as part of a digital card so i need the image in a format for email as well as print. The brand uses a silver (foil block) on its logo and a specific pan tone ref olive green (reference 620). Not too religious and include a quirky message.

Target Market(s)

The target market is clients with investments. Typically more than £100,000 which is why the card needs to be very classy.

Industry/Entity Type

Religious

Requirements
Must have
• logo - but i can't work out how to attach it! i can email it tho. contact me on mira@tarvexlink.com

```html
<!DOCTYPE html>
<html lang="en">
<head>
<meta charset="UTF-8">
<title>Seasons Greetings – Ardenwell Partners</title>
<link rel="stylesheet" href="https://fonts.googleapis.com/css2?family=Comfortaa:wght@300&display=swap">
<style>
  :root {
    --card-bg: #3e3936;
    --snow: #ffffff;
    --wreath-tone: rgba(255, 255, 255, 0.28);
    --panel-bg: #4a4643;
    --olive: #8a7d36;
    --text-light: #f4f2ef;
  }
  html, body {
    margin: 0;
    padding: 0;
    width: 847px;
    height: 1200px;
    overflow: hidden;
    background: var(--card-bg);
  }
  .card {
    position: relative;
    width: 847px;
    height: 1200px;
    overflow: hidden;
    background: var(--card-bg);
    font-family: "Comfortaa", sans-serif;
    font-weight: 300;
    color: var(--text-light);
  }
  .wreath {
    position: absolute;
    left: 0;
    top: 0;
    width: 847px;
    height: 1200px;
  }
  .greeting {
    position: absolute;
    left: 300px;
    top: 380px;
    width: 496px;
    text-align: center;
    margin: 0;
  }
  .greeting-title {
    display: block;
    font-size: 56px;
    line-height: 1.1;
    letter-spacing: 0.5px;
  }
  .greeting-sub {
    display: block;
    font-size: 40px;
    line-height: 1.2;
    margin-left: -10px;
  }
  .brand {
    position: absolute;
    left: 262px;
    top: 1019px;
    width: 323px;
    height: 114px;
    background: var(--panel-bg);
    border-bottom: 8px solid var(--olive);
    box-sizing: border-box;
    display: flex;
    align-items: center;
    justify-content: center;
  }
  .brand-name {
    font-family: "Comfortaa", sans-serif;
    font-weight: 300;
    font-size: 24px;
    letter-spacing: 7px;
    color: var(--text-light);
  }
</style>
</head>
<body>
  <main class="card">
    <svg class="wreath" viewBox="0 0 847 1200" role="img" aria-label="Wreath of white decorative snowflake ornaments arranged in a large circle">
      <circle cx="494" cy="434" r="383" fill="none" stroke="var(--wreath-tone)" stroke-width="200"/>
    </svg>

    <h1 class="greeting">
      <span class="greeting-title">Seasons Greetings</span>
      <span class="greeting-sub">from us all</span>
    </h1>

    <div class="brand">
      <span class="brand-name">ARDENWELL</span>
    </div>
  </main>
</body>
</html>
```